Poster for a Bicycle show/Expo

We need a poster for a Bicycle show/Expo and sustainable transport. Exhibitors will sell bikes, cycling clothing, accessories, etc. ...
This show is annual and the Poster is for the 2015 edition.

The style must be modern, dynamic, bright colors.

Your concept must be compatible in a landscape format. (We will ourselves adaptations of different formats.)
Width: 210 mm
Height: 297 mm
It's necessary for us to have the source file (vector) for make, later, the different format (flyers, website, ...)

Content of the Poster:
- 1 big picture (no clip art)
- Big title: « Fête Roulix » (« Salon » or « Salon du » can be small and « Vélo » big.)
- Subtitle: « et de la mobilité douce »
- Date: « 8, 9 et 10 mai 2015 » or « 8-10 mai 2015 »
- Place: « Halle TRX - Quai Brenaz »
- Text line 1: « www.fete-roulix.ch - Entrée gratuite »
- Text line 2« Piste d’essais - Restauration sur place »
- Text line 3: « Ve 8 mai de 17h à 21h - Sa 9 mai de 10h à 20h - Di 10 mai de 10h à 18h »
- Please, leave a zone in the poster for sponsors logos
(The predominant information (most visible) are: « Fête Roulix » and « 8, 9 et 10 mai 2015 or 8-10 mai 2015 »)

Content of the big picture:
- from a cheap stock, like PixoBanq.com
- a bicycle in action or a detail of a bicycle (or a accessory) (no race bike)
- a modern picture with bright colors.
- if a person is on the picture, we prefer a men
- not an aerial view with cyclists in a landscape.

Some examples of poster of shows - with typo-title worked

http://www.bassinexpoville.com/Temp/IMG/F_a7c2e9b4d1f0836255e1b7a9c4d3f2e6812c9b0a4e5f7_200_296.png

http://qz4m.tolvanfoires.fr/Data/kmtolv_mer/block/F_9bd1c3e7f2a4605813c9e2d7b4a8f6c0d3e1a527f86c2.pdf
(page 2 of this PDF)

http://salons.marvelle-agenda.fr/images/marvelle-agenda/foires-salons/phototheque/expo-moto-brivanne/expo-moto-brivanne2012-affiche.jpg

http://www.drupaix.net/blog/wp-content/uploads/2007/03/affiche-foire-des-pages.jpg

http://www.voilemarine-club.com/wp-content/affiche-regate-2007.jpg

Hello,

For information, for your next versions, please, add the text "Piste d'essais".

- Text line 1: « www.fete-roulix.ch - Entrée gratuite »
- Text line 2: « Piste d’essais - Restauration sur place »
- Text line 3: « Ve 8 mai de 17h à 21h - Sa 9 mai de 10h à 20h - Di 10 mai de 10h à 18h »

Thanks,
Mathieu

Landscape

Sans Serif

```html
<!DOCTYPE html>
<html lang="fr">
<head>
<meta charset="utf-8">
<title>Fête Roulix et de la mobilité douce — 8-10 mai 2015</title>
<link rel="stylesheet" href="https://fonts.googleapis.com/css2?family=Bebas+Neue&display=swap">
<style>
  :root {
    --backdrop: #e8e8e8;
    --paper: #ffffff;
    --ink: #111111;
    --lime: #b6cd1a;
    --teal: #5bbfc7;
    --charcoal: #333333;
    --steel-light: #eef0f2;
    --steel-mid: #b9bec4;
    --steel-dark: #5e6369;
  }
  * { margin: 0; padding: 0; box-sizing: border-box; }
  html, body {
    width: 1200px; height: 1152px; overflow: hidden;
    background: var(--backdrop);
    font-family: "Bebas Neue", "Arial Narrow", sans-serif;
  }
  .poster {
    position: absolute; left: 0; top: 152px;
    width: 1200px; height: 848px;
    background: var(--paper); overflow: hidden;
  }
  .hero-photo {
    position: absolute; left: 660px; top: 0; width: 540px; height: 741px;
    background: radial-gradient(ellipse at 60% 45%, var(--steel-light) 0%, var(--steel-mid) 55%, var(--steel-dark) 100%);
    clip-path: polygon(10% 0, 100% 0, 100% 100%, 4% 100%, 0 60%);
  }
  .band { position: absolute; left: 0; }
  .band--subtitle { top: 455px; height: 51px; width: 982px; background: var(--lime); }
  .band--info { top: 526px; height: 84px; width: 1200px; background: var(--teal); }
  .title-small {
    position: absolute; left: 66px; top: 60px;
    font-size: 68px; line-height: 1; color: var(--ink); letter-spacing: 1px;
  }
  .title-big {
    position: absolute; left: 60px; top: 101px;
    font-size: 330px; line-height: 1; color: var(--ink); letter-spacing: -3px;
  }
  .subtitle {
    position: absolute; left: 84px; top: 457px;
    font-size: 52px; line-height: 1; color: var(--paper); letter-spacing: 0.5px;
  }
  .event-date, .event-place {
    position: absolute; left: 84px;
    font-size: 37px; line-height: 1; color: var(--paper); letter-spacing: 0.5px;
  }
  .event-date { top: 532px; }
  .event-place { top: 571px; }
  .sponsors { position: absolute; left: 0; top: 630px; width: 660px; height: 100px; }
  .sponsor {
    position: absolute; display: flex; align-items: center; gap: 8px;
    font-size: 30px; line-height: 1; color: var(--ink); letter-spacing: 1px;
  }
  .sponsor-mark { width: 20px; height: 20px; background: var(--ink); }
  .sponsor-mark--round { border-radius: 50%; }
  .info-bar {
    position: absolute; left: 0; top: 741px; width: 1200px; height: 56px;
    background: var(--charcoal); color: var(--paper);
    display: flex; align-items: center; justify-content: center;
    font-size: 31px; letter-spacing: 0.5px;
  }
  .opening-hours {
    position: absolute; left: 0; top: 813px; width: 1200px; text-align: center;
    font-size: 30px; line-height: 1; color: var(--teal); letter-spacing: 0.5px;
  }
  .dot { margin: 0 10px; }
</style>
</head>
<body>
  <main class="poster">
    <div class="hero-photo" role="img" aria-label="Photo en gros plan d'un vélo argenté : roue avant, pneu, frein et cadre chromé"></div>
    <div class="band band--subtitle"></div>
    <div class="band band--info"></div>

    <h1>
      <span class="title-small">FÊTE</span>
      <span class="title-big">ROULIX</span>
    </h1>
    <p class="subtitle">ET DE LA MOBILITÉ DOUCE</p>
    <p class="event-date">8-10 MAI 2015</p>
    <p class="event-place">HALLE TRX - QUAI BRENAZ</p>

    <section class="sponsors" aria-label="Partenaires">
      <div class="sponsor" style="left:27px; top:10px;"><span class="sponsor-mark"></span>QUIMBREL</div>
      <div class="sponsor" style="left:205px; top:10px;">VOSTRAKEL</div>
      <div class="sponsor" style="left:403px; top:33px;"><span class="sponsor-mark"></span>FRENZOLL</div>
      <div class="sponsor" style="left:545px; top:33px;"><span class="sponsor-mark sponsor-mark--round"></span>ZELPKO</div>
      <div class="sponsor" style="left:27px; top:60px;">DRUVEX</div>
      <div class="sponsor" style="left:212px; top:60px;">PLONDRIKA</div>
    </section>

    <div class="info-bar">WWW.FETE-ROULIX.CH - ENTRÉE GRATUITE - RESTAURATION SUR PLACE - PISTE D'ESSAIS</div>
    <p class="opening-hours">VE 8 MAI DE 17H À 21H<span class="dot">•</span>SA 9 MAI DE 10H À 20H<span class="dot">•</span>DI 10 MAI DE 10H À 18H</p>
  </main>
</body>
</html>
```